Recruitment Site Design

We need a design for the login page, about page, and inner pages of a recruitment site for an oil and gas company. Design should be modern, sleek, professional and colors can be blue, green, white, orange or any other recommended colors.

Please also take into consideration that once the users login, they will need to access a form to fill in their information.

** UPDATE: Kindly provide a design for the inner information page consistent with the outer design. Attached is a picture of the basic structure. ***
Updates

Please provide a design for inner pages as shown in the design brief consistent with the registration page provided. 

Reason: We're extending it to get more inside pages.

Target Market(s)

Professionals looking for a career in the oil and gas industry in the Middle East.

Industry/Entity Type

Oil And Gas

Requirements
Must have
• Sleek design

```html
<!DOCTYPE html>
<html lang="en">
<head>
<meta charset="utf-8">
<title>Recruitment Site – Home</title>
<link href="https://fonts.googleapis.com/css2?family=Ropa+Sans&family=Open+Sans:wght@400;600&display=swap" rel="stylesheet">
<style>
:root{
  --orange:#e08a1e;
  --orange-dark:#c8710f;
  --orange-light:#f2a73a;
  --panel:#eeeef2;
  --text:#4a4a4a;
  --muted:#6b6b6b;
  --white:#ffffff;
  --line:#d8d8de;
}
*{box-sizing:border-box;margin:0;padding:0}
html,body{width:806px;height:1200px;overflow:hidden;background:var(--white)}
body{position:relative;font-family:"Open Sans",sans-serif;color:var(--text)}
.abs{position:absolute}

.brand{left:91px;top:40px;font-family:"Ropa Sans",sans-serif;font-size:45px;color:var(--orange);line-height:1}

.search{left:555px;top:57px;width:164px;height:30px;border:1px solid #d5d5d5;border-radius:15px;background:var(--white);box-shadow:inset 0 1px 3px rgba(0,0,0,.12);overflow:hidden}
.search span{position:absolute;left:10px;top:7px;font-size:11px;color:#666}
.search-btn{position:absolute;right:0;top:0;width:40px;height:100%;background:linear-gradient(var(--orange-light),var(--orange-dark));border-radius:0 15px 15px 0}

.nav{left:86px;top:98px;width:634px;height:41px;background:linear-gradient(#f0a640,var(--orange) 50%,#d47c14);border:1px solid #fff;box-shadow:0 0 0 1px #e2e2e2,0 2px 4px rgba(0,0,0,.15);display:flex;border-radius:2px}
.nav a{font-family:"Ropa Sans",sans-serif;font-size:14px;color:var(--white);text-decoration:none;display:flex;align-items:center;justify-content:center;border-right:1px solid rgba(160,90,10,.45);text-shadow:0 1px 1px rgba(0,0,0,.3)}
.nav a:last-child{border-right:0}
.nav a.current{color:#4a3210;text-shadow:0 1px 0 rgba(255,255,255,.3)}

.slider{left:85px;top:154px;width:636px;height:305px;background:var(--white);box-shadow:0 0 4px rgba(0,0,0,.15)}
.slide-art{position:absolute;left:9px;top:12px;width:618px;height:285px;background:linear-gradient(#4f86c8 0%,#a9c9e8 55%,#e7edf2 80%,#7d8a6a 100%)}
.slider-shadow{left:120px;top:460px;width:566px;height:18px;background:radial-gradient(ellipse at top,rgba(0,0,0,.14),rgba(0,0,0,0) 70%)}
.dots{left:403px;top:475px;display:flex;gap:3px}
.dots i{width:5px;height:5px;border-radius:50%;background:#777}
.dots i.on{background:var(--orange)}

.main-panel{left:88px;top:541px;width:632px;height:614px;background:var(--panel);border:1px solid #fff;box-shadow:0 0 3px rgba(0,0,0,.18)}

.features{left:115px;top:508px;width:581px;height:271px;background:var(--orange);border-radius:3px;box-shadow:0 2px 5px rgba(0,0,0,.3);display:flex}
.feature{position:relative;flex:1;text-align:center;color:var(--white)}
.feature+.feature:before{content:"";position:absolute;left:0;top:20px;bottom:20px;border-left:1px dashed rgba(255,255,255,.45)}
.feature-photo{width:84px;height:84px;border-radius:50%;margin:17px auto 0;border:3px solid #9a5a12;box-shadow:0 0 0 2px #f4b766}
.feature h3{font-family:"Ropa Sans",sans-serif;font-weight:400;font-size:15px;margin-top:9px;color:#fff}
.feature p{width:146px;margin:3px auto 0;font-size:11px;line-height:15.3px;text-align:justify;text-align-last:left;color:#fff8ee}
.more{display:inline-block;margin-top:12px;width:56px;height:27px;line-height:26px;border-radius:12px;background:linear-gradient(#fff,#d6d6d6);box-shadow:0 2px 3px rgba(0,0,0,.35);font-family:"Ropa Sans",sans-serif;font-size:14px;color:#555}

.welcome{left:116px;top:804px;width:320px}
.welcome h2{font-family:"Ropa Sans",sans-serif;font-weight:400;font-size:19px;color:var(--orange);padding-bottom:6px;border-bottom:1px solid var(--line)}
.welcome p{font-size:11.6px;line-height:19.8px;text-align:justify;margin-top:6px}
.welcome p .lead{color:var(--orange-dark);font-weight:600}

.login{left:462px;top:803px;width:232px;height:331px;background:#f7f7f9;border:1px solid #dcdce0;border-radius:10px;box-shadow:0 1px 4px rgba(0,0,0,.12)}
.ribbon{position:absolute;left:40px;width:152px;height:64px}
.ribbon span{position:absolute;left:0;right:0;text-align:center;font-family:"Ropa Sans",sans-serif;font-size:17px;color:#fff;text-shadow:0 1px 1px rgba(0,0,0,.3)}
.field{position:absolute;left:21px;width:188px;height:34px;border:1px solid #dedede;border-radius:10px;background:#f3f3f5;padding:9px 8px;font-size:13px;color:#555}
.btn-login{position:absolute;left:72px;top:178px;width:87px;height:33px;background:var(--orange);border-radius:3px;color:#fff;font-size:14px;text-align:center;line-height:33px;box-shadow:0 1px 2px rgba(0,0,0,.2)}
.not-member{position:absolute;left:0;right:0;top:242px;text-align:center;font-size:13px;color:#555}

.footer{left:300px;top:1167px;width:240px;text-align:center;font-size:9.5px;line-height:14px;color:#444}
.footer u{text-decoration:underline}
.social{left:573px;top:1166px;display:flex;gap:3px}
.social i{width:14px;height:14px;background:#b5682a;border-radius:2px}
</style>
</head>
<body>

<div class="abs brand">Logo Here</div>

<div class="abs search"><span>Search</span>
  <div class="search-btn">
    <svg width="40" height="30" viewBox="0 0 40 30"><circle cx="19" cy="13" r="5.5" fill="none" stroke="#fff" stroke-width="2"/><line x1="23" y1="17" x2="27" y2="21" stroke="#fff" stroke-width="2.5" stroke-linecap="round"/></svg>
  </div>
</div>

<nav class="abs nav">
  <a class="current" style="width:117px">Home</a>
  <a style="width:117px">About Us</a>
  <a style="width:107px">Find Job</a>
  <a style="width:143px">Register Here</a>
  <a style="flex:1">Contact Us</a>
</nav>

<div class="abs slider">
  <div class="slide-art" role="img" aria-label="Field engineer in orange coveralls holding a laptop beside oil pumpjacks under a cloudy blue sky"></div>
</div>
<div class="abs slider-shadow"></div>
<div class="abs dots"><i class="on"></i><i></i><i></i></div>

<div class="abs main-panel"></div>

<section class="abs features">
  <div class="feature">
    <div class="feature-photo" role="img" aria-label="Businessman at a desk with a laptop" style="background:linear-gradient(#fafafa,#d9dde4)"></div>
    <h3>About Us</h3>
    <p>We need a design for the login page, about page, and inner pages of a recruitment site for an oil and gas company. Design should be modern, sleek, professional.</p>
    <span class="more">More</span>
  </div>
  <div class="feature">
    <div class="feature-photo" role="img" aria-label="Businessman with clasped hands" style="background:linear-gradient(#2c3548,#c98a6a)"></div>
    <h3>Developement</h3>
    <p>We need a design for the login page, about page, and inner pages of a recruitment site for an oil and gas company. Design should be modern, sleek, professional.</p>
    <span class="more">More</span>
  </div>
  <div class="feature">
    <div class="feature-photo" role="img" aria-label="Business handshake" style="background:linear-gradient(135deg,#2f3f6a,#f3f3f3 55%,#d9a07a)"></div>
    <h3>Recruitement</h3>
    <p>We need a design for the login page, about page, and inner pages of a recruitment site for an oil and gas company. Design should be modern, sleek, professional.</p>
    <span class="more">More</span>
  </div>
</section>

<section class="abs welcome">
  <h2>Welcome to our site</h2>
  <p>We need a design for the login page, about page, and inner pages of a recruitment site for an oil and gas company. Design should be modern, sleek, professional and colors can be blue, green, white, orange or any other recommended colors. We need a design for the login page, about page, and inner pages of a recruitment site for an oil and gas company. Design should be modern, sleek, professional and colors can be blue, green, white, orange or any other recommended colors.
  <span class="lead">We need a design for the login page, about page, and inner pages of a recruitment site for an oil and gas company.</span>
  Design should be modern, sleek, professional and colors can be blue, green, white, orange or any other recommended colors. We need a design for the login page, about page, and inner pages.We need a design for the login page, about page, and inner pages.</p>
</section>

<aside class="abs login">
  <div class="ribbon" style="top:-1px">
    <svg width="152" height="64" viewBox="0 0 152 64">
      <defs><linearGradient id="ribbonTop" x1="0" y1="0" x2="0" y2="1"><stop offset="0" stop-color="#f5b640"/><stop offset="1" stop-color="#d27712"/></linearGradient></defs>
      <path d="M0 0 H152 L128 56 Q76 70 24 56 Z" fill="#fff" stroke="#e0e0e0"/>
      <path d="M10 0 H142 L122 50 Q76 62 30 50 Z" fill="url(#ribbonTop)"/>
    </svg>
    <span style="top:26px">Login Now</span>
  </div>
  <div class="field" style="top:84px">User Name</div>
  <div class="field" style="top:132px">Password</div>
  <div class="btn-login">Login</div>
  <div class="not-member">Not a Member?</div>
  <div class="ribbon" style="top:266px">
    <svg width="152" height="64" viewBox="0 0 152 64">
      <defs><linearGradient id="ribbonBottom" x1="0" y1="0" x2="0" y2="1"><stop offset="0" stop-color="#f5b640"/><stop offset="1" stop-color="#d27712"/></linearGradient></defs>
      <path d="M24 8 Q76 -6 128 8 L152 64 H0 Z" fill="#fff" stroke="#e0e0e0"/>
      <path d="M30 14 Q76 2 122 14 L142 64 H10 Z" fill="url(#ribbonBottom)"/>
    </svg>
    <span style="top:24px">Register Here</span>
  </div>
</aside>

<footer class="abs footer">Copyright @ 2012, <u>Company Name</u><br>Terms &amp; Privacy Policy</footer>
<div class="abs social" aria-label="Social links"><i></i><i></i></div>

</body>
</html>
```